Business Card Design for a Sound engineer and DJ

We would like a residn of the business card.

Logo must remain the same.
The card is for the owner of the company.
The business card is in Arabic as the company is based in Kuwait.
The company specializes in sound engineering for singers concerts and events and in addition DJ.
The color options is up to the designer but we would like it masculine as the owner is a man.

Target Market(s)

All ages

Industry/Entity Type

Media

Contact Information for Business Card

Name:
Eng. Tarek Halabi
م/طارق حلبي

The name above is in Arabic and English.

Title: General Manager
Mobile: +965 66307852
Office: +965 22486037
Email: info@sawtarin.net

Address:
Office no. 3
1st floor
Almarfa Complex
Rashed AlQeblawi St.
Salmiya
Kuwait

Instagram: @sawtarin
Snap: sawtarin

Requirements
Nice to have
• can we have Instagram icon and snap icon and a phone vector and email?
• Instead of writing the words

```html
<!DOCTYPE html>
<html lang="en">
<head>
<meta charset="utf-8">
<title>Sawtarin – Business Card Back</title>
<link rel="stylesheet" href="https://fonts.googleapis.com/css2?family=Carlito&family=Saira+Condensed:wght@600;700&family=Cairo:wght@600;700&display=swap">
<style>
  :root {
    --page: #ffffff;
    --card: #0b0c0e;
    --ink-light: #ffffff;
    --brand-purple: #7d3e93;
    --brand-magenta: #b23c8e;
    --brand-violet: #8a6fc2;
    --brand-faint: #24192a;
    --brand-faint-2: #1b1a24;
  }
  * { margin: 0; padding: 0; box-sizing: border-box; }
  html, body {
    width: 1200px; height: 707px; overflow: hidden;
    background: var(--page);
  }
  .card {
    position: relative;
    width: 1200px; height: 707px;
    background: var(--card);
    border-radius: 34px;
    overflow: hidden;
    font-family: "Carlito", "Calibri", sans-serif;
  }

  /* social handles */
  .social { position: absolute; left: 42px; top: 38px; }
  .social-row {
    display: flex; align-items: center; gap: 20px;
    height: 46px; margin-bottom: 15px;
    color: var(--ink-light); font-size: 36px; line-height: 1;
  }
  .social-mark { width: 40px; height: 40px; flex: none; display: block; }

  /* faint background echo of the wordmark */
  .echo { position: absolute; left: 0; top: 0; width: 1200px; height: 707px; }
  .echo-mark {
    position: absolute; left: 30px; top: 140px;
    font-family: "Saira Condensed", sans-serif; font-weight: 700;
    font-size: 230px; line-height: 1; color: var(--brand-faint-2);
    letter-spacing: 6px;
  }
  .echo-name {
    position: absolute; left: -8px; top: 510px;
    font-family: "Saira Condensed", sans-serif; font-weight: 700;
    font-size: 84px; line-height: 1; letter-spacing: 34px;
    color: var(--brand-faint);
  }
  .echo-tagline {
    position: absolute; left: -4px; top: 620px;
    font-family: "Saira Condensed", sans-serif; font-weight: 700;
    font-size: 44px; letter-spacing: 8px; line-height: 1;
    color: var(--brand-faint);
  }
  .echo-tagline-ar {
    position: absolute; left: 10px; top: 672px;
    font-family: "Cairo", sans-serif; font-weight: 700;
    font-size: 36px; line-height: 1; color: var(--brand-faint);
    direction: rtl;
  }

  /* brand block */
  .brand-mark {
    position: absolute; right: 62px; top: 150px;
    display: flex; align-items: center; gap: 22px;
  }
  .brand-mark-square { width: 40px; height: 40px; background: var(--brand-violet); }
  .brand-mark-name {
    font-family: "Saira Condensed", sans-serif; font-weight: 700;
    font-size: 190px; line-height: 1.1; color: var(--brand-violet);
    direction: rtl;
  }
  .brand-name {
    position: absolute; left: 628px; top: 490px; width: 530px;
    font-family: "Saira Condensed", sans-serif; font-weight: 700;
    font-size: 72px; line-height: 1; letter-spacing: 28px;
    color: var(--brand-purple);
  }
  .brand-tagline {
    position: absolute; right: 44px; top: 572px;
    font-family: "Saira Condensed", sans-serif; font-weight: 700;
    font-size: 37px; line-height: 1; letter-spacing: 5px;
    color: var(--brand-purple);
  }
  .brand-tagline-ar {
    position: absolute; right: 44px; top: 614px;
    font-family: "Cairo", sans-serif; font-weight: 700;
    font-size: 34px; line-height: 1.3; direction: rtl;
    color: var(--brand-purple);
  }
</style>
</head>
<body>
  <div class="card">

    <div class="echo" aria-hidden="true">
      <div class="echo-mark">صوتارين</div>
      <div class="echo-name">SAWTARIN</div>
      <div class="echo-tagline">DJ - SOUND ENG. - LIGHTING</div>
      <div class="echo-tagline-ar">دي جي - هندسة صوت - إضاءة</div>
    </div>

    <div class="social">
      <div class="social-row">
        <svg class="social-mark" viewBox="0 0 40 40" aria-hidden="true"><circle cx="20" cy="20" r="17" fill="var(--ink-light)"/></svg>
        <span class="social-handle">/ sawtarin</span>
      </div>
      <div class="social-row">
        <svg class="social-mark" viewBox="0 0 40 40" aria-hidden="true"><rect x="3" y="3" width="34" height="34" rx="4" fill="var(--ink-light)"/></svg>
        <span class="social-handle">@sawtarin</span>
      </div>
    </div>

    <div class="brand-mark">
      <div class="brand-mark-square" aria-hidden="true"></div>
      <div class="brand-mark-name">صوتارين</div>
    </div>
    <div class="brand-name">SAWTARIN</div>
    <div class="brand-tagline">DJ - SOUND ENG. - LIGHTING</div>
    <div class="brand-tagline-ar">دي جي - هندسة صوت - إضاءة</div>

  </div>
</body>
</html>
```